Design a For Sale sign board and Direction Sign Board.
Attached is an example of what i am thinking but am happy to look at any options.
Colours are to be ""bright Orange"on white and in reverse as well.

Logo id Fairbrook & Co Real Estate.

```html
<!DOCTYPE html>
<html lang="en">
<head>
<meta charset="utf-8">
<title>Fairbrook &amp; Co Real Estate – Sale and Direction Signs</title>
<link rel="stylesheet" href="https://fonts.googleapis.com/css2?family=Arimo:wght@400;700&display=swap">
<style>
  :root {
    --orange: #f49a1a;
    --orange-edge: #f07800;
    --white: #ffffff;
    --page: #efebe6;
    --font: "Arimo", Arial, sans-serif;
  }
  * { box-sizing: border-box; margin: 0; padding: 0; }
  html, body {
    width: 1200px;
    height: 1200px;
    overflow: hidden;
    background: var(--page);
    font-family: var(--font);
  }
  .canvas {
    position: relative;
    width: 1200px;
    height: 1200px;
  }
  .sign {
    position: absolute;
    width: 456px;
    height: 284px;
    border: 8px solid var(--orange-edge);
    border-radius: 26px;
    overflow: hidden;
    background: var(--top);
  }
  .sign--light { --top: var(--white); --band: var(--orange); --top-ink: var(--orange); --band-ink: var(--white); }
  .sign--bold  { --top: var(--orange); --band: var(--white); --top-ink: var(--white); --band-ink: var(--orange); }

  .sign--sale-light  { left: 96px;  top: 246px; }
  .sign--arrow-light { left: 642px; top: 246px; }
  .sign--sale-bold   { left: 96px;  top: 624px; }
  .sign--arrow-bold  { left: 642px; top: 624px; }

  .band {
    position: absolute;
    inset: 0;
    width: 100%;
    height: 100%;
  }
  .band path { fill: var(--band); }

  .brand {
    position: absolute;
    left: 0;
    right: 0;
    top: 40px;
    text-align: center;
    color: var(--top-ink);
    font-weight: 700;
    line-height: 1;
  }
  .brand__name {
    display: block;
    font-size: 38px;
    letter-spacing: 0.5px;
  }
  .brand__trade {
    display: block;
    margin-top: 8px;
    font-size: 18px;
    letter-spacing: 2px;
    text-transform: uppercase;
    text-align: right;
    padding-right: 62px;
  }

  .agent {
    position: absolute;
    left: 0;
    right: 0;
    text-align: center;
    color: var(--band-ink);
    line-height: 1;
  }
  .agent__name {
    top: 180px;
    font-size: 24px;
    font-weight: 400;
  }
  .agent__phone {
    top: 212px;
    font-size: 29px;
    font-weight: 700;
    letter-spacing: 2.5px;
  }

  .corner-mark {
    position: absolute;
    bottom: 22px;
    width: 44px;
    height: 44px;
    background: var(--band-ink);
  }
  .corner-mark--left { left: 22px; }
  .corner-mark--right { right: 22px; }

  .arrow {
    position: absolute;
    left: 100px;
    top: 208px;
    width: 240px;
    height: 30px;
    color: var(--band-ink);
  }
</style>
</head>
<body>
<svg width="0" height="0" style="position:absolute" aria-hidden="true">
  <defs>
    <symbol id="arrow-left" viewBox="0 0 240 30">
      <path d="M18 15 H236" stroke="currentColor" stroke-width="6"/>
      <path d="M2 15 L22 2 L22 28 Z" fill="currentColor"/>
    </symbol>
  </defs>
</svg>

<main class="canvas">

  <section class="sign sign--light sign--sale-light" aria-label="For sale sign, white top">
    <svg class="band" viewBox="0 0 456 284" preserveAspectRatio="none" aria-hidden="true"><path d="M0 140 Q228 200 456 140 V284 H0 Z"/></svg>
    <div class="brand"><span class="brand__name">Fairbrook &amp; Co</span><span class="brand__trade">Real Estate</span></div>
    <p class="agent agent__name">Daniel Hart</p>
    <p class="agent agent__phone">0400 118 274</p>
    <span class="corner-mark corner-mark--left" aria-hidden="true"></span>
    <span class="corner-mark corner-mark--right" aria-hidden="true"></span>
  </section>

  <section class="sign sign--light sign--arrow-light" aria-label="Direction sign, white top">
    <svg class="band" viewBox="0 0 456 284" preserveAspectRatio="none" aria-hidden="true"><path d="M0 140 Q228 200 456 140 V284 H0 Z"/></svg>
    <div class="brand"><span class="brand__name">Fairbrook &amp; Co</span><span class="brand__trade">Real Estate</span></div>
    <p class="agent agent__name">Daniel Hart</p>
    <svg class="arrow" aria-hidden="true"><use href="#arrow-left"/></svg>
    <span class="corner-mark corner-mark--left" aria-hidden="true"></span>
    <span class="corner-mark corner-mark--right" aria-hidden="true"></span>
  </section>

  <section class="sign sign--bold sign--sale-bold" aria-label="For sale sign, orange top">
    <svg class="band" viewBox="0 0 456 284" preserveAspectRatio="none" aria-hidden="true"><path d="M0 140 Q228 200 456 140 V284 H0 Z"/></svg>
    <div class="brand"><span class="brand__name">Fairbrook &amp; Co</span><span class="brand__trade">Real Estate</span></div>
    <p class="agent agent__name">Daniel Hart</p>
    <p class="agent agent__phone">0400 118 274</p>
    <span class="corner-mark corner-mark--left" aria-hidden="true"></span>
    <span class="corner-mark corner-mark--right" aria-hidden="true"></span>
  </section>

  <section class="sign sign--bold sign--arrow-bold" aria-label="Direction sign, orange top">
    <svg class="band" viewBox="0 0 456 284" preserveAspectRatio="none" aria-hidden="true"><path d="M0 140 Q228 200 456 140 V284 H0 Z"/></svg>
    <div class="brand"><span class="brand__name">Fairbrook &amp; Co</span><span class="brand__trade">Real Estate</span></div>
    <p class="agent agent__name">Daniel Hart</p>
    <svg class="arrow" aria-hidden="true"><use href="#arrow-left"/></svg>
    <span class="corner-mark corner-mark--left" aria-hidden="true"></span>
    <span class="corner-mark corner-mark--right" aria-hidden="true"></span>
  </section>

</main>
</body>
</html>
```